Thornwell Building Company - advertisement poster

I am looking to print some canvas signs to advertise my general contracting company, Thornwell Building Company. The sign will measure 6' long x 3' high so the size should match that ratio. I already have a logo icon, which is the Letter 'T' and some trees that I would like to incorporate, see attached. I would also like the to have the following information listed:
1) phone number: 472-555-0188
2) email: thornwellbuildingcompany@mailvero.com
3) website: thornwellbuildingcompany.com
4) Lic#4620385
5) I want to use this text: "BUILD WITH THE T-CREW!"

The ad should be relatively simple and clean. Black and Green are my company colors. I am open to creative ideas!

Target Market(s)

People looking to renovate their homes

Industry/Entity Type

Construction

Colors
59FF00
82FF00
B8FF75
E3FFCB
F4FFEA

Requirements
Must have
• Must have my company logo
Should not have
• No photos or complex graphics

```html
<!DOCTYPE html>
<html lang="en">
<head>
<meta charset="utf-8">
<title>Thornwell Building Company – Sign</title>
<link rel="stylesheet" href="https://fonts.googleapis.com/css2?family=Bebas+Neue&family=Montserrat:ital,wght@0,500;0,700;1,700;1,800&display=swap">
<style>
  :root {
    --backdrop: #ececec;
    --green: #72b446;
    --green-dark: #41672a;
    --green-light: #a5d38d;
    --black: #000000;
    --white: #ffffff;
  }
  html, body {
    margin: 0;
    padding: 0;
    width: 1200px;
    height: 684px;
    overflow: hidden;
    background: var(--backdrop);
  }
  .sign { display: block; width: 1200px; height: 684px; }
  .tagline { font-family: "Bebas Neue", "Oswald", sans-serif; }
  .tagline-build { fill: var(--green); }
  .tagline-dark { fill: var(--black); }
  .brand-text { font-family: "Montserrat", Arial, sans-serif; font-weight: 700; fill: var(--white); }
  .estd-text { font-family: "Montserrat", Arial, sans-serif; font-weight: 500; fill: var(--white); letter-spacing: 6px; }
  .license-text { font-family: "Montserrat", Arial, sans-serif; font-weight: 500; fill: var(--white); }
  .phone-number { font-family: "Montserrat", Arial, sans-serif; font-weight: 800; font-style: italic; fill: var(--white); }
  .contact-text { font-family: "Montserrat", Arial, sans-serif; font-weight: 700; font-style: italic; fill: var(--white); }
</style>
</head>
<body>
<svg class="sign" viewBox="0 0 2555 1456" xmlns="http://www.w3.org/2000/svg" role="img" aria-label="Thornwell Building Company sign: Build with the T-Crew! Call 472-555-0188">
  <!-- banner base -->
  <rect class="banner" x="163" y="162" width="2230" height="1132" fill="var(--green)"/>

  <!-- left black wedge -->
  <polygon class="wedge-left" points="163,162 447,162 1118,728 447,1294 163,1294" fill="var(--black)"/>
  <!-- dark green stripe -->
  <polygon class="stripe-dark" points="1118,728 1128,770 505,1294 447,1294" fill="var(--green-dark)"/>
  <!-- bottom contact band -->
  <polygon class="contact-band" points="1070,887 2393,887 2393,1294 613,1294" fill="var(--black)"/>

  <!-- house outline -->
  <polygon class="house-shade" points="1717,310 1748,298 2349,532 2208,532 2208,887 2157,887 2157,532 2283,532" fill="var(--green-light)"/>
  <polygon class="house" points="1147,532 1717,310 2283,532 2157,532 2157,887 1288,887 1288,532" fill="var(--white)"/>

  <!-- hammer illustration area -->
  <rect class="hammer-art" x="1630" y="360" width="190" height="100" rx="20" fill="var(--black)" opacity="0.85" role="img" aria-label="Hammer illustration"/>

  <!-- tagline -->
  <text class="tagline tagline-build" x="1462" y="648" font-size="230" textLength="383" lengthAdjust="spacingAndGlyphs">BUILD</text>
  <text class="tagline tagline-dark" x="1875" y="565" font-size="104" textLength="158" lengthAdjust="spacingAndGlyphs">WITH</text>
  <text class="tagline tagline-dark" x="1875" y="652" font-size="104" textLength="118" lengthAdjust="spacingAndGlyphs">THE</text>
  <text class="tagline tagline-dark" x="1420" y="825" font-size="218" textLength="660" lengthAdjust="spacingAndGlyphs"><tspan class="tagline-build">T-</tspan>CREW!</text>

  <!-- brand block -->
  <line x1="239" y1="633" x2="333" y2="633" stroke="var(--white)" stroke-width="3"/>
  <line x1="239" y1="672" x2="333" y2="672" stroke="var(--green)" stroke-width="3"/>
  <text class="estd-text" x="286" y="661" font-size="26" text-anchor="middle">ESTD</text>
  <line x1="731" y1="633" x2="825" y2="633" stroke="var(--white)" stroke-width="3"/>
  <line x1="731" y1="672" x2="825" y2="672" stroke="var(--green)" stroke-width="3"/>
  <text class="estd-text" x="778" y="661" font-size="26" text-anchor="middle">2020</text>

  <circle class="brand-dot" cx="534" cy="625" r="62" fill="var(--green)"/>

  <text class="brand-text" x="210" y="793" font-size="86" textLength="645" lengthAdjust="spacingAndGlyphs">THORNWELL</text>
  <text class="brand-text" x="213" y="836" font-size="38" textLength="642" lengthAdjust="spacing">BUILDING COMPANY</text>

  <rect class="license-pill" x="366" y="869" width="336" height="80" rx="36" fill="none" stroke="var(--green)" stroke-width="7"/>
  <text class="license-text" x="534" y="924" font-size="44" text-anchor="middle">LIC#4620385</text>

  <!-- phone -->
  <circle cx="1292" cy="1028" r="99" fill="none" stroke="var(--green)" stroke-width="8"/>
  <g class="icon-phone" fill="var(--white)">
    <path d="M1250,990 c-14,8 -20,22 -12,42 c12,30 34,52 62,66 c18,9 32,2 40,-10 l-22,-22 c-6,-5 -12,-4 -16,1 l-8,8 c-14,-7 -30,-23 -37,-37 l8,-8 c5,-4 6,-10 1,-16 z"/>
    <path d="M1300,1000 a18,18 0 0 1 18,18" fill="none" stroke="var(--white)" stroke-width="8" stroke-linecap="round"/>
    <path d="M1302,983 a35,35 0 0 1 35,35" fill="none" stroke="var(--white)" stroke-width="8" stroke-linecap="round"/>
  </g>
  <text class="phone-number" x="1450" y="1075" font-size="142" textLength="890" lengthAdjust="spacingAndGlyphs">472-555-0188</text>

  <!-- web -->
  <circle cx="913" cy="1194" r="33" fill="none" stroke="var(--green)" stroke-width="6"/>
  <g class="icon-globe" fill="none" stroke="var(--white)" stroke-width="3">
    <circle cx="911" cy="1193" r="15"/>
    <ellipse cx="911" cy="1193" rx="6" ry="15"/>
    <line x1="896" y1="1193" x2="926" y2="1193"/>
  </g>
  <text class="contact-text" x="982" y="1204" font-size="29" textLength="540" lengthAdjust="spacingAndGlyphs">THORNWELLBUILDINGCOMPANY.COM</text>
  <line x1="982" y1="1214" x2="1522" y2="1214" stroke="var(--green)" stroke-width="4"/>

  <!-- email -->
  <circle cx="1611" cy="1194" r="33" fill="none" stroke="var(--green)" stroke-width="6"/>
  <circle cx="1611" cy="1194" r="20" fill="var(--white)"/>
  <g class="icon-mail" fill="none" stroke="var(--black)" stroke-width="2">
    <rect x="1602" y="1188" width="18" height="12"/>
    <polyline points="1602,1188 1611,1195 1620,1188"/>
  </g>
  <text class="contact-text" x="1677" y="1204" font-size="29" textLength="663" lengthAdjust="spacingAndGlyphs">THORNWELLBUILDINGCOMPANY@MAILVERO.COM</text>
  <line x1="1677" y1="1214" x2="2340" y2="1214" stroke="var(--green)" stroke-width="4"/>
</svg>
</body>
</html>
```